Kovalen Spinal Care and Performance

We need new business cards, something more modern, clean. On the back of the card maybe a quote. The Dr. likes, “The doctor of the future will give no medicine, but will interest his patient in the care of the human frame, in diet and in the cause and prevention of disease.” - Walter Brisby. We are open to other suggestions. We are a chiropractic office.

```html
<!DOCTYPE html>
<html lang="en">
<head>
<meta charset="utf-8">
<title>Kovalen Spinal Care and Performance — Business Card</title>
<link rel="stylesheet" href="https://fonts.googleapis.com/css2?family=Cinzel:wght@400&family=Raleway:wght@300;400&display=swap">
<style>
  :root {
    --backdrop: #e9e6e1;
    --card-white: #fbfbfa;
    --purple: #6b3a80;
    --purple-deep: #57276b;
    --purple-light: #7d4d92;
    --green: #9dc23a;
    --ink-grey: #5a5a5a;
    --quote-white: #f1e9f4;
  }
  * { margin: 0; padding: 0; box-sizing: border-box; }
  html, body { width: 1200px; height: 859px; overflow: hidden; background: var(--backdrop); }
  .canvas { position: relative; width: 1200px; height: 859px; }
  .card {
    position: absolute; top: 289px; width: 500px; height: 284px;
    border-radius: 12px; overflow: hidden;
    box-shadow: 0 6px 14px rgba(0,0,0,0.25);
  }
  .card--front { left: 60px; background: var(--card-white); }
  .card--back {
    left: 639px;
    background: radial-gradient(ellipse at 20% 10%, var(--purple-light), var(--purple) 55%, var(--purple-deep));
  }
  .card__shapes { position: absolute; inset: 0; }

  .wordmark { position: absolute; font-family: "Cinzel", serif; font-weight: 400; color: var(--purple); line-height: 1; }
  .wordmark__name { display: block; letter-spacing: 1px; }
  .wordmark__tagline { display: block; font-family: "Raleway", sans-serif; font-weight: 400; letter-spacing: 0.2px; }

  .card--front .wordmark { left: 62px; top: 122px; }
  .card--front .wordmark__name { font-size: 31px; }
  .card--front .wordmark__tagline { font-family: "Cinzel", serif; font-size: 8.4px; margin-top: 4px; }

  .divider { position: absolute; left: 250px; top: 102px; width: 1px; height: 84px; background: var(--green); }
  .contact { position: absolute; left: 262px; top: 100px; }
  .contact__name { font-family: "Cinzel", serif; font-size: 17.5px; color: var(--purple); letter-spacing: 0.6px; line-height: 1.1; }
  .contact__role { font-family: "Raleway", sans-serif; font-size: 13.5px; color: var(--ink-grey); margin-bottom: 6px; }
  .contact__line { display: flex; align-items: center; gap: 6px; font-family: "Raleway", sans-serif; font-size: 13.8px; color: var(--ink-grey); line-height: 17px; margin-left: -10px; }
  .contact__icon { width: 12px; height: 12px; flex: none; }

  .card--back .wordmark { right: 28px; top: 38px; text-align: right; color: #ffffff; }
  .card--back .wordmark__name { font-size: 36px; }
  .card--back .wordmark__tagline { font-family: "Cinzel", serif; font-size: 9.5px; margin-top: 5px; }

  .quote { position: absolute; right: 27px; top: 134px; text-align: right; font-family: "Raleway", sans-serif; }
  .quote__lead { font-size: 25px; font-weight: 400; color: var(--green); line-height: 1.1; margin-bottom: 6px; }
  .quote__text { font-size: 12.6px; font-weight: 300; color: var(--quote-white); line-height: 17px; }
  .quote__author { font-family: "Cinzel", serif; font-size: 16px; color: var(--quote-white); letter-spacing: 0.8px; margin-top: 10px; }
</style>
</head>
<body>
<main class="canvas">
  <section class="card card--front" aria-label="Card front">
    <svg class="card__shapes" viewBox="0 0 500 284" width="500" height="284" aria-hidden="true">
      <path d="M325 0 Q430 14 500 42 L500 0 Z" fill="var(--green)"/>
      <path d="M345 0 Q440 16 500 34 L500 0 Z" fill="var(--purple)"/>
      <path d="M0 268 Q250 262 500 240 L500 284 L0 284 Z" fill="var(--green)"/>
    </svg>
    <div class="wordmark">
      <span class="wordmark__name">KOVALEN</span>
      <span class="wordmark__tagline">SPINAL CARE &amp; PERFORMANCE</span>
    </div>
    <div class="divider"></div>
    <div class="contact">
      <div class="contact__name">WALTER BRISBY</div>
      <div class="contact__role">The Doctor</div>
      <div class="contact__line">
        <svg class="contact__icon" viewBox="0 0 12 12"><circle cx="6" cy="6" r="5.2" fill="none" stroke="var(--purple)" stroke-width="1"/><path d="M4 3.3 L5 4.6 L4.5 5.3 Q5.2 6.8 6.7 7.5 L7.4 7 L8.7 8 Q8 9 7 8.9 Q4 8 3.2 5 Q3.1 4 4 3.3 Z" fill="var(--purple)"/></svg>
        604-555-0142
      </div>
      <div class="contact__line">
        <svg class="contact__icon" viewBox="0 0 12 12"><rect x="1" y="2.5" width="10" height="7" fill="none" stroke="var(--purple)" stroke-width="1"/><path d="M1 2.5 L6 6.5 L11 2.5" fill="none" stroke="var(--purple)" stroke-width="1"/></svg>
        info@kovalenspinal.com
      </div>
      <div class="contact__line">
        <svg class="contact__icon" viewBox="0 0 12 12"><circle cx="6" cy="6" r="5" fill="none" stroke="var(--purple)" stroke-width="1"/><ellipse cx="6" cy="6" rx="2.2" ry="5" fill="none" stroke="var(--purple)" stroke-width="0.9"/><path d="M1 6 H11 M2 3.5 H10 M2 8.5 H10" stroke="var(--purple)" stroke-width="0.8"/></svg>
        www.kovalenspinal.com
      </div>
    </div>
  </section>

  <section class="card card--back" aria-label="Card back">
    <div class="wordmark">
      <span class="wordmark__name">KOVALEN</span>
      <span class="wordmark__tagline">SPINAL CARE &amp; PERFORMANCE</span>
    </div>
    <div class="quote">
      <div class="quote__lead">The Dr. likes,</div>
      <p class="quote__text">The doctor of the future will give no medicine,<br>but will interest his patient in the care of the human frame,<br>in diet and in the cause and prevention of disease.</p>
      <div class="quote__author">WALTER BRISBY</div>
    </div>
  </section>
</main>
</body>
</html>
```